Notepads for Marketing pieces-BOLD design

Looking for notepads for marketing pieces with logo, phone number, and website. Maybe something faded in background. Looking for bold and different

```html
<!DOCTYPE html>
<html lang="en">
<head>
<meta charset="utf-8">
<title>Vitalis Care Notepad</title>
<link href="https://fonts.googleapis.com/css2?family=Montserrat:wght@500;600;700;800&display=swap" rel="stylesheet">
<style>
  :root {
    --brand-red: #ff0000;
    --ink-red: #e8000b;
    --black: #000000;
    --white: #ffffff;
    --divider: rgba(0, 0, 0, 0.18);
  }
  * { margin: 0; padding: 0; box-sizing: border-box; }
  html, body {
    width: 848px;
    height: 1200px;
    overflow: hidden;
    background: var(--white);
  }
  .notepad {
    position: relative;
    width: 848px;
    height: 1200px;
    background: var(--white);
    font-family: "Montserrat", sans-serif;
  }
  .masthead {
    position: absolute;
    top: 0; left: 0;
    width: 100%;
    height: 154px;
    background: var(--brand-red);
    text-align: center;
    color: var(--white);
  }
  .brand-name {
    position: absolute;
    top: 44px;
    left: 0; right: 0;
    font-weight: 800;
    font-size: 40px;
    letter-spacing: 2px;
    line-height: 1;
  }
  .services {
    position: absolute;
    top: 115px;
    left: 0; right: 0;
    font-weight: 700;
    font-size: 10.5px;
    line-height: 1;
  }
  .contact-block {
    position: absolute;
    top: 1022px;
    left: 0; right: 0;
    text-align: center;
    color: var(--ink-red);
    font-size: 13.5px;
    font-weight: 500;
    line-height: 24.2px;
  }
  .contact-block .company { font-weight: 700; }
  .social-bar {
    position: absolute;
    left: 0; bottom: 0;
    width: 100%;
    height: 46px;
    display: flex;
  }
  .social-item {
    flex: 1;
    display: flex;
    align-items: center;
    justify-content: center;
    gap: 12px;
    color: var(--white);
    font-size: 14.5px;
    font-weight: 500;
    background: var(--brand-red);
  }
  .social-item + .social-item { border-left: 1px solid var(--divider); }
  .social-item.is-dark { background: var(--black); border-left: none; }
  .social-mark {
    width: 16px;
    height: 16px;
    background: var(--white);
    border-radius: 2px;
  }
</style>
</head>
<body>
  <main class="notepad">
    <header class="masthead">
      <div class="brand-name">VITALIS CARE</div>
      <div class="services">Home Health | Medical Staffing | Outpatient Therapy</div>
    </header>

    <section class="contact-block">
      <div class="company">Vitalis Therapy Partners</div>
      <div>www.vitaliscare.org</div>
      <div>admin@vitaliscare.org</div>
      <div>555.014.2290 555.014.7731</div>
      <div>480 Meridian Lane Fairview,OH 45000</div>
    </section>

    <footer class="social-bar">
      <div class="social-item"><span class="social-mark"></span>vitaliscare</div>
      <div class="social-item"><span class="social-mark"></span>@vitaliscarellc</div>
      <div class="social-item is-dark"><span class="social-mark"></span>vitaliscare</div>
    </footer>
  </main>
</body>
</html>
```